Business cards

Design business cards for our company. Just a straight, business like design with the logo, name, function and contact details

Target Market(s)

We are a innovative technological company active in water treatment

Industry/Entity Type

Water management

Contact Information for Business Card

Name, Function, email, telephone number, link to website

```html
<!DOCTYPE html>
<html lang="en">
<head>
<meta charset="UTF-8">
<title>Wavelume Business Cards</title>
<link href="https://fonts.googleapis.com/css2?family=Comfortaa:wght@400;700&display=swap" rel="stylesheet">
<style>
  :root {
    --bg: #76767c;
    --card-light: #ffffff;
    --card-dark: #2a2a2c;
    --brand-blue: #2f95d8;
    --text-grey: #8c8c8c;
    --text-dark: #3a3a3a;
    --faint-blue: #e3ecf7;
    --faint-dark: #343436;
  }
  * { margin: 0; padding: 0; box-sizing: border-box; }
  html, body { width: 1200px; height: 900px; overflow: hidden; }
  body {
    background: var(--bg);
    font-family: "Comfortaa", sans-serif;
    display: flex;
    flex-direction: column;
    align-items: center;
    justify-content: center;
    gap: 40px;
  }
  .card {
    position: relative;
    width: 700px;
    height: 400px;
    border-radius: 22px;
    overflow: hidden;
  }
  .card--front { background: var(--card-light); }
  .card--back { background: var(--card-dark); }

  .brand { display: flex; align-items: center; gap: 14px; }
  .brand__name {
    font-weight: 700;
    color: var(--brand-blue);
    line-height: 1;
  }
  .brand__dot { border-radius: 50%; background: var(--text-grey); }
  .brand__tagline {
    color: var(--text-grey);
    letter-spacing: 0.06em;
    text-transform: uppercase;
  }

  .card--front .decor {
    position: absolute; right: -60px; top: -70px;
    width: 360px; height: 360px; border-radius: 50%;
    background: var(--faint-blue);
  }
  .card--front .brand-block { position: absolute; left: 48px; top: 70px; }
  .card--front .brand__name { font-size: 62px; }
  .card--front .brand__dot { width: 36px; height: 36px; }
  .card--front .brand__tagline { font-size: 17px; margin-top: 8px; }

  .person { position: absolute; left: 48px; top: 205px; }
  .person__name { font-size: 30px; color: var(--brand-blue); }
  .person__role { font-size: 20px; color: var(--text-grey); margin-top: 4px; }

  .contact { list-style: none; margin-top: 16px; }
  .contact__item {
    display: flex; align-items: center; gap: 12px;
    font-size: 17px; color: var(--text-dark); margin-bottom: 7px;
  }
  .contact__icon { width: 16px; height: 16px; flex: none; }

  .card--back .decor {
    position: absolute; left: -90px; bottom: -120px;
    width: 340px; height: 340px; border-radius: 50%;
    background: var(--faint-dark);
  }
  .card--back .brand-block {
    position: absolute; left: 0; right: 0; top: 120px;
    display: flex; flex-direction: column; align-items: center;
  }
  .card--back .brand__name { font-size: 66px; }
  .card--back .brand__dot { width: 40px; height: 40px; }
  .card--back .brand__tagline { font-size: 19px; margin-top: 10px; color: #9a9a9a; }
  .card--back .url {
    position: absolute; left: 0; right: 0; bottom: 60px;
    text-align: center; font-size: 20px; color: var(--brand-blue);
  }
</style>
</head>
<body>
  <section class="card card--front">
    <div class="decor"></div>
    <div class="brand-block">
      <div class="brand">
        <span class="brand__name">Wavelume</span>
        <span class="brand__dot"></span>
      </div>
      <div class="brand__tagline">Nanobubble Technology</div>
    </div>
    <div class="person">
      <div class="person__name">Marcus Ellery</div>
      <div class="person__role">CEO/Founder</div>
      <ul class="contact">
        <li class="contact__item">
          <svg class="contact__icon" viewBox="0 0 16 16"><path d="M4 1l3 3-2 2c1 2 3 4 5 5l2-2 3 3-2 3C7 15 1 9 1 3z" fill="#2f95d8"/></svg>
          555-013-4782
        </li>
        <li class="contact__item">
          <svg class="contact__icon" viewBox="0 0 16 16"><rect x="1" y="3" width="14" height="10" rx="1" fill="#2f95d8"/><path d="M1 4l7 5 7-5" stroke="#fff" stroke-width="1.4" fill="none"/></svg>
          marcus@mailbox-demo.com
        </li>
        <li class="contact__item">
          <svg class="contact__icon" viewBox="0 0 16 16"><circle cx="8" cy="8" r="7" fill="#2f95d8"/><path d="M1 8h14M8 1c-3 4-3 10 0 14M8 1c3 4 3 10 0 14" stroke="#fff" stroke-width="1" fill="none"/></svg>
          www.demo-site-link.com
        </li>
      </ul>
    </div>
  </section>

  <section class="card card--back">
    <div class="decor"></div>
    <div class="brand-block">
      <div class="brand">
        <span class="brand__name">Wavelume</span>
        <span class="brand__dot"></span>
      </div>
      <div class="brand__tagline">Nanobubble Technology</div>
    </div>
    <div class="url">www.Wavelume.com</div>
  </section>
</body>
</html>
```